Lumora Signal Website

Looking for a website design that clearly and powerfully portrays our unique and effective indoor advertising billboards in our network.

Our Classic Billboards and Wall Boards are strategically placed in high traffic areas of restaurants, pubs, nightclubs, fitness clubs, colleges & universities, and sports facilities.

Lumora Signal Group is our new name. Our current site is www.brevanopromo.ca
with our focus being entirely on our Out-of-Home Media Networks.

New website address will be www.lumorasignal.ca

We need the following sections:
HOME

PRODUCTS (Drop down menu)
-Classic Billboards
-Wall Boards

NETWORKS (Drop down menu)
-Resto-Bar
-Sports
-Campus
-Casino

FEATURES

CAMPAIGNS

BECOME A PARTNER

CONTACT

Please include social media functions on the homepage such as twitter/facebook/linkdin

We will be supplying content and photos as required.

Our plan is to have you submit the homepage design to start with, and then we can start judging which styles we like the best and can start narrowing our list.

As a second round, we would like to ask the "finalists" to submit a second page (another section of the website) and to see how consistent you are in terms of the look and feel you proposed for the homepage.

Attached is our new logo.

Target Market(s)

Small Business Owners, Advertising Agencies, Media Buyers, Marketing Managers

Industry/Entity Type

Media

Number of Pages Required

1 page

Font styles to use
Sans Serif

Requirements
Must have
• Our Unique Network offers advertising solutions that feature:
• Guaranteed Readership,100% Gender Specific, Frequency, and Captive Audience. Purchasing advertising space in our network are small to medium business owners and advertising agencies booking on behalf of their clients.
• Site must be professional and modern looking.

```html
<!DOCTYPE html>
<html lang="en">
<head>
<meta charset="utf-8">
<title>Lumora Signal Group</title>
<link href="https://fonts.googleapis.com/css2?family=Nunito+Sans:wght@300;400;600;700;800&display=swap" rel="stylesheet">
<style>
:root{
  --red:#c8080d;
  --red-dark:#a50206;
  --white:#ffffff;
  --ink:#222222;
  --muted:#7a7a7a;
  --light:#f1f1f1;
  --footer:#f3f3f3;
  --rule:#d6d6d6;
  --btn:#7b7b7b;
  --social:#2a7bbf;
}
*{margin:0;padding:0;box-sizing:border-box}
html,body{width:1200px;height:2605px;overflow:hidden}
body{position:relative;background:var(--white);font-family:"Nunito Sans",Arial,sans-serif;color:var(--ink)}
.abs{position:absolute}

/* header */
.brand{left:118px;top:34px;display:flex;align-items:center;gap:10px;color:var(--red);font-size:30px;font-weight:700;letter-spacing:.2px}
.brand-dot{width:28px;height:28px;border-radius:50%;background:var(--red)}
.social{top:54px;width:34px;height:34px;border-radius:50%;background:var(--social)}
.main-nav{left:0;top:116px;width:1200px;height:52px;background:linear-gradient(var(--red),var(--red-dark))}
.main-nav a{position:absolute;top:14px;color:var(--white);font-size:18px;text-decoration:none;transform:translateX(-50%);white-space:nowrap}
.main-nav a.active::after{content:"";position:absolute;left:-4px;right:-4px;bottom:-11px;height:3px;background:var(--white)}

/* hero */
.hero{left:0;top:168px;width:1200px;height:506px;background:radial-gradient(circle at 72% 45%,#a88a63 0,#5a4632 14%,transparent 30%),linear-gradient(100deg,#1e2326 0%,#3a2a24 30%,#6b2b1e 45%,#23272d 70%,#151a1e 100%)}
.hero-title{left:122px;top:330px;color:var(--white);font-weight:700;line-height:1}
.hero-title .big{display:block;font-size:56px;margin-bottom:2px}
.hero-title .sub{display:block;font-size:34px;margin-top:6px}
.dot{top:643px;width:14px;height:14px;border-radius:50%;background:var(--white)}
.dot.off{background:transparent;border:2px solid var(--white)}

/* intro */
.intro-title{left:0;width:1200px;top:720px;text-align:center;font-size:33px;font-weight:400;line-height:38px}
.intro-text{left:180px;width:840px;top:818px;text-align:center;font-size:15px;line-height:26px;color:#555}
.btn-grey{left:535px;top:894px;width:130px;height:39px;background:var(--btn);color:var(--white);font-size:15px;text-align:center;line-height:39px}

/* networks */
.networks{left:0;top:969px;width:1200px;height:424px;background:var(--light)}
.section-title{font-size:31px;font-weight:400}
.net-title{left:134px;top:1030px}
.net-text{left:134px;top:1082px;width:470px;font-size:14.5px;line-height:26px;color:var(--muted)}
.net-card{top:1181px;width:140px;height:106px;background:var(--white);border:1px solid #dcdcdc;text-align:center;color:var(--red);font-size:15px}
.net-card svg{display:block;margin:16px auto 6px}
.screen{left:653px;top:1038px;width:434px;height:256px;background:#111;padding:8px}
.screen-art{width:100%;height:100%;background:linear-gradient(135deg,#d7ecef 0%,#8fc3cc 45%,#3e8d9d 100%)}
.leg{top:1294px;width:16px;height:95px;background:#111}

/* products */
.products{left:0;top:1393px;width:1200px;height:384px;background:linear-gradient(180deg,var(--red),#b80207)}
.prod-title{left:0;width:1200px;top:1432px;text-align:center;color:var(--white)}
.prod-icon{top:1528px;width:128px;height:128px;border-radius:50%;background:var(--white);display:flex;align-items:center;justify-content:center}
.prod-name{top:1522px;color:var(--white);font-size:23px;font-weight:400}
.prod-text{top:1560px;width:278px;color:var(--white);font-size:13.5px;line-height:22px}
.btn-outline{top:1655px;width:116px;height:33px;border:1.5px solid var(--white);color:var(--white);font-size:14px;text-align:center;line-height:30px}

/* campaigns */
.camp-title{left:0;width:1200px;top:1815px;text-align:center}
.camp-card{top:1888px;width:255px;height:311px;background:var(--white);border:1px solid #d8d8d8;box-shadow:0 1px 4px rgba(0,0,0,.15);padding:11px}
.camp-art{width:100%;height:100%}
.art-purple{background:linear-gradient(180deg,#6a2b7e,#4e1d62)}
.art-yellow{background:linear-gradient(180deg,#f7c51c,#f1b80e)}
.art-dark{background:linear-gradient(180deg,#dfe6ee 0%,#9aa6b4 45%,#b1151b 65%,#1d2430 100%)}

/* footer */
.footer{left:0;top:2263px;width:1200px;height:342px;background:var(--footer)}
.foot-col{top:2320px}
.foot-col h4{font-size:24px;font-weight:400;color:#333;margin-bottom:12px}
.foot-col li{list-style:none;font-size:15px;line-height:26.5px;color:#666}
.contact-line{display:flex;align-items:center;gap:10px}
.foot-rule{left:125px;top:2534px;width:950px;height:1px;background:var(--rule)}
.copyright{left:0;width:1200px;top:2547px;text-align:center;font-size:13px;color:#777}
</style>
</head>
<body>

<header>
  <div class="abs brand"><span class="brand-dot"></span>Lumora Signal Group</div>
  <span class="abs social" style="left:959px" aria-label="Social profile link"></span>
  <span class="abs social" style="left:1001px" aria-label="Social profile link"></span>
  <span class="abs social" style="left:1041px" aria-label="Social profile link"></span>
  <nav class="abs main-nav">
    <a class="active" href="#" style="left:174px">Home</a>
    <a href="#" style="left:290px">Products</a>
    <a href="#" style="left:420px">Networks</a>
    <a href="#" style="left:551px">Features</a>
    <a href="#" style="left:689px">Campaigns</a>
    <a href="#" style="left:867px">Become a Partner</a>
    <a href="#" style="left:1030px">Contact</a>
  </nav>
</header>

<section>
  <div class="abs hero" role="img" aria-label="Night city street with light trails and an illuminated billboard showing a perfume ad"></div>
  <h1 class="abs hero-title"><span class="big">OVER 1000</span><span class="big">BILLBOARDS</span><span class="sub">3 TARGETED NETWORKS</span></h1>
  <span class="abs dot off" style="left:552px"></span>
  <span class="abs dot" style="left:576px"></span>
  <span class="abs dot" style="left:601px"></span>
  <span class="abs dot" style="left:625px"></span>
</section>

<section>
  <h2 class="abs intro-title">Our Unique Network offers advertising<br>Solutions that feature:</h2>
  <p class="abs intro-text">Guaranteed Readership,100% Gender Specific, Frequency, and Captive Audience. Purchasing advertising space in our<br>network are small to medium business owners and advertising agencies booking on behalf of their clients.</p>
  <div class="abs btn-grey">Learn More</div>
</section>

<section>
  <div class="abs networks"></div>
  <h2 class="abs section-title net-title">Our Networks</h2>
  <p class="abs net-text">Donec dictum lectus non odio Cras a ante vitae enim iaculis aliquam<br>Mauris nunc quam venenatis nec euismod sit amet egestas placerat est<br>Pellentesque habitant morbi tristique senectus et</p>
  <div class="abs net-card" style="left:134px">
    <svg width="40" height="46" viewBox="0 0 40 46" fill="none" stroke="#c8080d" stroke-width="3"><ellipse cx="20" cy="8" rx="12" ry="5"/><line x1="20" y1="13" x2="20" y2="40"/><line x1="10" y1="42" x2="30" y2="42"/><line x1="13" y1="28" x2="27" y2="28"/></svg>
    RESTO BAR
  </div>
  <div class="abs net-card" style="left:275px">
    <svg width="52" height="44" viewBox="0 0 52 44" fill="none" stroke="#c8080d" stroke-width="3"><rect x="3" y="3" width="46" height="38"/><line x1="26" y1="3" x2="26" y2="41"/><circle cx="26" cy="22" r="6"/><rect x="3" y="14" width="8" height="16"/><rect x="41" y="14" width="8" height="16"/></svg>
    SPORTS
  </div>
  <div class="abs net-card" style="left:416px">
    <svg width="56" height="46" viewBox="0 0 56 46" fill="none" stroke="#c8080d" stroke-width="3"><path d="M4 44V20h14V8l10-5 10 5v12h14v24z"/><rect x="23" y="30" width="10" height="14"/><rect x="24" y="12" width="8" height="8"/><rect x="8" y="26" width="6" height="6"/><rect x="42" y="26" width="6" height="6"/></svg>
    CAMPUS
  </div>
  <div class="abs screen"><div class="screen-art" role="img" aria-label="Billboard showing a skincare tube splashing in water"></div></div>
  <span class="abs leg" style="left:761px"></span>
  <span class="abs leg" style="left:969px"></span>
</section>

<section>
  <div class="abs products"></div>
  <h2 class="abs section-title prod-title">Our Products</h2>

  <div class="abs prod-icon" style="left:144px">
    <svg width="60" height="54" viewBox="0 0 60 54" fill="none" stroke="#c8080d" stroke-width="3"><rect x="4" y="4" width="52" height="30"/><line x1="4" y1="4" x2="56" y2="34"/><line x1="18" y1="34" x2="12" y2="50"/><line x1="42" y1="34" x2="48" y2="50"/></svg>
  </div>
  <h3 class="abs prod-name" style="left:302px">Classic Billboards</h3>
  <p class="abs prod-text" style="left:302px">Curabitur iaculis tempus eros Curabitur vel mi sit amet magna malesuada ultrices Ut nisi erat fermentum vel congue id euismod in elit Fusce ultricies orci ac feugiat</p>
  <div class="abs btn-outline" style="left:304px">View Ads</div>

  <div class="abs prod-icon" style="left:634px">
    <svg width="54" height="54" viewBox="0 0 54 54" fill="none" stroke="#c8080d" stroke-width="3"><rect x="4" y="8" width="46" height="38"/><rect x="14" y="16" width="26" height="22"/><line x1="4" y1="4" x2="50" y2="4"/><line x1="4" y1="50" x2="50" y2="50"/></svg>
  </div>
  <h3 class="abs prod-name" style="left:794px">Wall Billboards</h3>
  <p class="abs prod-text" style="left:794px">Curabitur iaculis tempus eros Curabitur vel mi sit amet magna malesuada ultrices Ut nisi erat fermentum vel congue id euismod in elit Fusce ultricies orci ac feugiat</p>
  <div class="abs btn-outline" style="left:794px">View Ads</div>
</section>

<section>
  <h2 class="abs section-title camp-title">Our Campaigns</h2>
  <svg class="abs" style="left:150px;top:2020px" width="22" height="38" viewBox="0 0 22 38" fill="none" stroke="#bbbbbb" stroke-width="4"><polyline points="19,3 4,19 19,35"/></svg>
  <div class="abs camp-card" style="left:188px"><div class="camp-art art-purple" role="img" aria-label="Smoothie shop poster with a bunch of bananas on purple"></div></div>
  <div class="abs camp-card" style="left:474px"><div class="camp-art art-yellow" role="img" aria-label="Yellow directory ad poster about finding local businesses"></div></div>
  <div class="abs camp-card" style="left:757px"><div class="camp-art art-dark" role="img" aria-label="Car dealership poster with a red car"></div></div>
  <svg class="abs" style="left:1027px;top:2020px" width="22" height="38" viewBox="0 0 22 38" fill="none" stroke="#bbbbbb" stroke-width="4"><polyline points="3,3 18,19 3,35"/></svg>
</section>

<footer>
  <div class="abs footer"></div>
  <div class="abs foot-col" style="left:139px"><h4>Company</h4><ul><li>Home</li><li>About Us</li><li>Why We Are</li><li>Our Campaigns</li></ul></div>
  <div class="abs foot-col" style="left:372px"><h4>Networks</h4><ul><li>Sports</li><li>Campus</li><li>Resto Bar</li></ul></div>
  <div class="abs foot-col" style="left:599px"><h4>Resources</h4><ul><li>Become a partner</li><li>Support</li><li>Products</li><li>Contact us</li></ul></div>
  <div class="abs foot-col" style="left:834px"><h4>Contact Us</h4><ul>
    <li>418 Harbor Point Lane Suite 12</li>
    <li>Westbrook, PA 19210</li>
    <li class="contact-line" style="margin-top:4px"><svg width="16" height="16" viewBox="0 0 24 24" fill="#c8080d"><path d="M6.6 10.8a15.1 15.1 0 006.6 6.6l2.2-2.2c.3-.3.7-.4 1-.2 1.1.4 2.3.6 3.6.6.6 0 1 .4 1 1V20c0 .6-.4 1-1 1A17 17 0 013 4c0-.6.4-1 1-1h3.5c.6 0 1 .4 1 1 0 1.3.2 2.5.6 3.6.1.3 0 .7-.2 1z"/></svg>(555) 304-7781</li>
    <li class="contact-line"><svg width="16" height="14" viewBox="0 0 24 20" fill="#c8080d"><path d="M2 2h20v16H2z"/><path d="M2 2l10 8 10-8" stroke="#fff" stroke-width="2" fill="none"/></svg>info@lumorasignal.ca</li>
  </ul></div>
  <div class="abs foot-rule"></div>
  <p class="abs copyright">© 2016 Company Name&nbsp; All right reserved</p>
</footer>

</body>
</html>
```